Minimalist Professional Business Card Design

We will be revamping our marketing materials: Business cards, Website and Catalogs.
Our Overall Design direction is to have a Minimalist artwork with Professionalism and Premium feel. The revamp starts with the new business card design followed by the others. Thus the designer whom work is selected for this job will likely to follow through with the subsequent jobs.

Target Market(s)

Upscale

Industry/Entity Type

Manufacturing

Contact Information for Business Card

For the Business Cards, the following are required:
. Minimalist yet Professional and Premium Feel
. Background Colors: white and / or light pastel yellow and if needed to smoothen the yellow, the light grey can be incorporated. We are changing our corporate bright yellow to either one of the three alternatives:
1. Soylant yellow CMYK (1%, 0%, 52%, 3%)
2. Popcorn yellow CMYK (0%, 0%, 33%, 0%)
3. Papaya yellow CMYK (0%, 0%, 51%, 0%)

Information to be inputed in the business cards:

Name: Barlen Moritova
Position: Managing Director

Company's name: Vellomar Valves Pte. Ltd.
Address: 512 Halvick Lane #07-09B
Singapore 617302
Tel: (65) 6281 4096
Fax: (65) 6294 7118
Email: barlen@vellomarvalves-example.com
Website: www.vellomarvalves-example.com
Callvox: Vellomar.Valves
Chatwell/ Lume/ Vibra/ Talkio: (65) 9372 6081

Company's Logo
Company's Slogan
Two product photos placed side by side (if this gets into the way of the design, it is OK not to include them)

Font styles to use
Serif

Colors
ffffff

Requirements
Must have
• Minimalist
Should not have
• Messy, crowded, playful

```html
<!DOCTYPE html>
<html lang="en">
<head>
<meta charset="utf-8">
<title>Vellomar Valves – Business Card</title>
<link rel="stylesheet" href="https://fonts.googleapis.com/css2?family=Jost:wght@500;600&family=Mulish:wght@400;600&display=swap">
<style>
  :root {
    --page: #a9a9a9;
    --card-white: #ededed;
    --pastel-yellow: #e2dc86;
    --logo-yellow: #e3dc84;
    --ink: #545454;
    --ink-soft: #5e5e5e;
    --band: #5b5b5b;
    --band-text: #f4f4f4;
  }
  * { margin: 0; padding: 0; box-sizing: border-box; }
  html, body { width: 1200px; height: 1024px; overflow: hidden; }
  body {
    background: var(--page);
    font-family: "Mulish", sans-serif;
    color: var(--ink);
    display: flex;
    align-items: center;
    justify-content: center;
    gap: 40px;
  }
  .card {
    position: relative;
    width: 540px;
    height: 300px;
    box-shadow: 0 2px 6px rgba(0,0,0,.25);
    overflow: hidden;
  }

  /* Contact side */
  .card--contact { background: var(--card-white); }
  .holder { position: absolute; left: 42px; top: 58px; }
  .holder__name {
    font-family: "Jost", sans-serif;
    font-weight: 600;
    font-size: 21px;
    letter-spacing: .2px;
    color: var(--ink);
  }
  .holder__title { font-size: 13px; margin-top: 2px; color: var(--ink-soft); }
  .divider {
    position: absolute; left: 42px; top: 148px;
    width: 40px; height: 1px; background: #9a9a9a;
  }
  .contact-list {
    position: absolute; left: 42px; top: 196px;
    list-style: none; font-size: 13px; color: var(--ink-soft);
  }
  .contact-list li { display: flex; align-items: center; gap: 8px; height: 19.5px; }
  .contact-list svg { width: 12px; height: 12px; flex: none; }
  .address {
    position: absolute; right: 40px; top: 235px;
    text-align: right; font-size: 13px; line-height: 19.5px;
    color: var(--ink-soft); font-style: normal;
  }
  .brand-mini {
    position: absolute; right: 40px; top: 42px;
    display: flex; align-items: center; gap: 6px;
    font-family: "Jost", sans-serif; font-weight: 600;
    font-size: 13px; letter-spacing: 1.5px; color: var(--logo-yellow);
  }
  .brand-mini__dot { width: 14px; height: 14px; border-radius: 50%; background: var(--logo-yellow); }

  /* Brand side */
  .card--brand { background: var(--pastel-yellow); }
  .brand {
    position: absolute; left: 0; right: 0; top: 42px;
    display: flex; flex-direction: column; align-items: center; gap: 12px;
  }
  .brand__circle {
    width: 108px; height: 108px; border-radius: 50%;
    border: 12px solid var(--ink);
  }
  .brand__name {
    font-family: "Jost", sans-serif; font-weight: 600;
    font-size: 44px; letter-spacing: 2px; line-height: 1; color: var(--ink);
  }
  .band {
    position: absolute; left: 0; right: 0; bottom: 0; height: 40px;
    background: var(--band); color: var(--band-text);
    display: flex; align-items: center; justify-content: center; gap: 12px;
    font-size: 12.5px; white-space: nowrap;
  }
</style>
</head>
<body>

  <section class="card card--contact" aria-label="Business card, contact side">
    <div class="brand-mini"><span class="brand-mini__dot"></span>VELLOMAR</div>

    <div class="holder">
      <h1 class="holder__name">Barlen Moritova</h1>
      <p class="holder__title">Managing Director</p>
    </div>

    <div class="divider"></div>

    <ul class="contact-list">
      <li>
        <svg viewBox="0 0 12 12" aria-hidden="true"><circle cx="6" cy="6" r="5.3" fill="none" stroke="#5e5e5e" stroke-width="1"/><path d="M4 3.3l1 1.2-.6.8a4 4 0 0 0 2.3 2.3l.8-.6 1.2 1-.5.9C6 8.8 3.3 6.1 3.2 3.8z" fill="#5e5e5e"/></svg>
        (65) 6281 4096
      </li>
      <li>
        <svg viewBox="0 0 12 12" aria-hidden="true"><circle cx="6" cy="6" r="5.3" fill="none" stroke="#5e5e5e" stroke-width="1"/><path d="M4 3.3l1 1.2-.6.8a4 4 0 0 0 2.3 2.3l.8-.6 1.2 1-.5.9C6 8.8 3.3 6.1 3.2 3.8z" fill="#5e5e5e"/></svg>
        (65) 6294 7118
      </li>
      <li>
        <svg viewBox="0 0 12 12" aria-hidden="true"><circle cx="6" cy="6" r="5.8" fill="#5e5e5e"/><rect x="3.3" y="4" width="5.4" height="4" fill="none" stroke="#ededed" stroke-width=".8"/><path d="M3.3 4L6 6.2 8.7 4" fill="none" stroke="#ededed" stroke-width=".8"/></svg>
        barlen@vellomarvalves-example.com
      </li>
      <li>
        <svg viewBox="0 0 12 12" aria-hidden="true"><circle cx="6" cy="6" r="5.3" fill="none" stroke="#5e5e5e" stroke-width="1"/><circle cx="6" cy="6" r="3" fill="#5e5e5e"/></svg>
        www.vellomarvalves-example.com
      </li>
    </ul>

    <address class="address">
      512 Halvick Lane #07-09B<br>
      Singapore 617302
    </address>
  </section>

  <section class="card card--brand" aria-label="Business card, brand side">
    <div class="brand">
      <div class="brand__circle"></div>
      <p class="brand__name">VELLOMAR</p>
    </div>
    <div class="band">
      <span>Callvox: Vellomar.Valves</span>
      <span>|</span>
      <span>Chatwell/ Lume/ Vibra/ Talkio: (65) 9372 6081</span>
    </div>
  </section>

</body>
</html>
```